New Flyer Design Project

I would like to purchase a customized version of a design you have previously submitted - https://www.plorvania.com/design/58204719

I want this to be something that looks really good.
We use this to explain our service agreements.
our website is www.bqumesh.net I want to stick with those colors.

```html
<!DOCTYPE html>
<html lang="en">
<head>
<meta charset="utf-8">
<title>BQM Support Plans</title>
<link rel="stylesheet" href="https://fonts.googleapis.com/css2?family=Poppins:wght@400;500;700;800&display=swap">
<style>
  :root {
    --brand-red: #d0232a;
    --brand-red-dark: #8c2326;
    --brand-grey: #5f6266;
    --text-body: #55585c;
    --rule: #d9dadd;
    --strip: #f6f7f9;
    --strip-text: #eceef1;
    --paper: #ffffff;
  }
  * { box-sizing: border-box; margin: 0; padding: 0; }
  html, body { width: 1200px; height: 829px; overflow: hidden; background: var(--paper); }
  body { font-family: "Poppins", sans-serif; position: relative; }

  .side-strip {
    position: absolute; left: 0; top: 0; width: 174px; height: 829px;
    background: var(--strip);
  }
  .side-strip__label {
    position: absolute; left: 64px; top: 784px;
    transform-origin: 0 0; transform: rotate(-90deg);
    font-weight: 800; font-size: 54px; line-height: 54px;
    color: var(--strip-text); white-space: nowrap; letter-spacing: 1px;
  }

  .flyer-title {
    position: absolute; left: 240px; top: 58px;
    font-weight: 800; font-size: 51px; letter-spacing: 0.5px;
    color: var(--brand-red); white-space: nowrap;
  }

  .brand {
    position: absolute; left: 938px; top: 72px; width: 200px;
  }
  .brand__name {
    display: flex; align-items: center; gap: 10px;
    font-weight: 700; font-size: 40px; line-height: 40px; color: var(--brand-grey);
  }
  .brand__dot { width: 18px; height: 18px; border-radius: 50%; background: var(--brand-red-dark); }
  .brand__tagline {
    margin-top: 6px; font-size: 11.5px; font-weight: 400; color: var(--brand-red-dark);
    white-space: nowrap;
  }

  .plans-header {
    position: absolute; left: 240px; top: 152px; width: 892px; height: 86px;
    border-radius: 14px 14px 0 0;
    background: linear-gradient(90deg, var(--brand-red-dark) 0%, #b0252a 55%, var(--brand-red) 100%);
    color: #fff; display: grid; grid-template-columns: 459px 220px 213px;
  }
  .plans-header__cell { display: flex; flex-direction: column; justify-content: center; white-space: nowrap; }
  .plans-header__cell + .plans-header__cell { border-left: 2px solid #fff; }
  .plans-header__services { padding-left: 44px; font-weight: 700; font-size: 26px; }
  .plans-header__plan { padding-left: 33px; font-weight: 700; font-size: 24px; line-height: 27px; }
  .plans-header__plan:last-child { padding-left: 21px; }
  .plans-header__price { font-size: 27px; }
  .plans-header__unit { font-size: 15px; }

  .plans-body {
    position: absolute; left: 240px; top: 238px; width: 892px; height: 563px;
    border: 1px solid var(--rule); border-top: none; border-radius: 0 0 24px 24px;
    padding-top: 8px;
  }
  .plans-body__divider {
    position: absolute; top: 0; bottom: 0; width: 1.5px; background: var(--rule);
  }
  .plans-body__divider--first { left: 458px; }
  .plans-body__divider--second { left: 678px; }

  .plan-row {
    height: 29.5px; display: grid; grid-template-columns: 459px 220px 213px;
    align-items: center;
  }
  .plan-row__service {
    padding-left: 48px; font-size: 14.8px; color: var(--text-body);
    white-space: nowrap; overflow: hidden;
  }
  .plan-row__mark {
    display: flex; justify-content: center; align-items: center;
    font-size: 14.5px; font-weight: 500; color: var(--brand-red);
    margin-top: -3px;
  }
  .tick { width: 17px; height: 17px; }
</style>
</head>
<body>
<svg width="0" height="0" style="position:absolute">
  <symbol id="tick" viewBox="0 0 20 20">
    <circle cx="10" cy="10" r="8.6" fill="none" stroke="#b9bbbf" stroke-width="1.2"/>
    <path d="M5.6 10.3 L8.7 13.3 L14.6 6.6" fill="none" stroke="#d0232a" stroke-width="2" stroke-linecap="round" stroke-linejoin="round"/>
  </symbol>
</svg>

<aside class="side-strip"><div class="side-strip__label">BQM SUPPORT PLANS</div></aside>

<h1 class="flyer-title">BQM SUPPORT PLANS</h1>

<div class="brand">
  <div class="brand__name">BQM <span class="brand__dot"></span></div>
  <div class="brand__tagline">bqumesh network solutions</div>
</div>

<div class="plans-header">
  <div class="plans-header__cell plans-header__services">Services</div>
  <div class="plans-header__cell plans-header__plan">Security Plus<span class="plans-header__price">$75.00</span></div>
  <div class="plans-header__cell plans-header__plan">IT Essentials<span class="plans-header__price">$55.00 <span class="plans-header__unit">Per PC</span></span></div>
</div>

<div class="plans-body">
  <div class="plans-body__divider plans-body__divider--first"></div>
  <div class="plans-body__divider plans-body__divider--second"></div>

  <div class="plan-row"><div class="plan-row__service">Unlimited US bases Remote Help Desk Support</div><div class="plan-row__mark"><svg class="tick"><use href="#tick"/></svg></div><div class="plan-row__mark"><svg class="tick"><use href="#tick"/></svg></div></div>
  <div class="plan-row"><div class="plan-row__service">Unlimited On-Site Support</div><div class="plan-row__mark"><svg class="tick"><use href="#tick"/></svg></div><div class="plan-row__mark">Available</div></div>
  <div class="plan-row"><div class="plan-row__service">Advanced Cybersecurity and Threat Hunting</div><div class="plan-row__mark"><svg class="tick"><use href="#tick"/></svg></div><div class="plan-row__mark">Available</div></div>
  <div class="plan-row"><div class="plan-row__service">Managed Antivirus Protection</div><div class="plan-row__mark"><svg class="tick"><use href="#tick"/></svg></div><div class="plan-row__mark"><svg class="tick"><use href="#tick"/></svg></div></div>
  <div class="plan-row"><div class="plan-row__service">Multifactor Authentication Powered by Vardekey</div><div class="plan-row__mark"><svg class="tick"><use href="#tick"/></svg></div><div class="plan-row__mark">Available</div></div>
  <div class="plan-row"><div class="plan-row__service">Cyber Security Awareness Training</div><div class="plan-row__mark"><svg class="tick"><use href="#tick"/></svg></div><div class="plan-row__mark">Available</div></div>
  <div class="plan-row"><div class="plan-row__service">Enhanced Span Filtering</div><div class="plan-row__mark"><svg class="tick"><use href="#tick"/></svg></div><div class="plan-row__mark">Available</div></div>
  <div class="plan-row"><div class="plan-row__service">Internet Content Filtering</div><div class="plan-row__mark"><svg class="tick"><use href="#tick"/></svg></div><div class="plan-row__mark">Available</div></div>
  <div class="plan-row"><div class="plan-row__service">Proactive Security and System Monitoring</div><div class="plan-row__mark"><svg class="tick"><use href="#tick"/></svg></div><div class="plan-row__mark"><svg class="tick"><use href="#tick"/></svg></div></div>
  <div class="plan-row"><div class="plan-row__service">Security and Vulnerability patching</div><div class="plan-row__mark"><svg class="tick"><use href="#tick"/></svg></div><div class="plan-row__mark"><svg class="tick"><use href="#tick"/></svg></div></div>
  <div class="plan-row"><div class="plan-row__service">Backup and disaster recovery</div><div class="plan-row__mark"><svg class="tick"><use href="#tick"/></svg></div><div class="plan-row__mark"><svg class="tick"><use href="#tick"/></svg></div></div>
  <div class="plan-row"><div class="plan-row__service">Network Management and Administration</div><div class="plan-row__mark"><svg class="tick"><use href="#tick"/></svg></div><div class="plan-row__mark"><svg class="tick"><use href="#tick"/></svg></div></div>
  <div class="plan-row"><div class="plan-row__service">Corvell Office Suite Administration and Configuration</div><div class="plan-row__mark"><svg class="tick"><use href="#tick"/></svg></div><div class="plan-row__mark"><svg class="tick"><use href="#tick"/></svg></div></div>
  <div class="plan-row"><div class="plan-row__service">Corvell Nimbus Administration and Configuration</div><div class="plan-row__mark"><svg class="tick"><use href="#tick"/></svg></div><div class="plan-row__mark"><svg class="tick"><use href="#tick"/></svg></div></div>
  <div class="plan-row"><div class="plan-row__service">Corvell Desktop and Server Support</div><div class="plan-row__mark"><svg class="tick"><use href="#tick"/></svg></div><div class="plan-row__mark"><svg class="tick"><use href="#tick"/></svg></div></div>
  <div class="plan-row"><div class="plan-row__service">Managed DNS</div><div class="plan-row__mark"><svg class="tick"><use href="#tick"/></svg></div><div class="plan-row__mark"><svg class="tick"><use href="#tick"/></svg></div></div>
  <div class="plan-row"><div class="plan-row__service">Hardware and Software Procurement</div><div class="plan-row__mark"><svg class="tick"><use href="#tick"/></svg></div><div class="plan-row__mark"><svg class="tick"><use href="#tick"/></svg></div></div>
  <div class="plan-row"><div class="plan-row__service">Assett Management</div><div class="plan-row__mark"><svg class="tick"><use href="#tick"/></svg></div><div class="plan-row__mark"><svg class="tick"><use href="#tick"/></svg></div></div>
</div>
</body>
</html>
```